Create Brisk Lesson Studio a card design that will stick in the mind of prospects.

Brisk Lesson Studio specialises designs and produces training video, animation, illustration and text.

We need a card design that oozes class and leaves the prospect brimming with confidence.

The design will feature the Brisk Lesson Studio all black logo (uploaded). The design may also use the shade of orange from the orange version of the logo (uploaded). Note, just the color is to be used e.g. for the back of the card, not the orange logo itself.

The Brisk brand is about authenticity, quality, maturity and assurance. We are a safe buy when it comes to the prospects next project.

Target Market(s)

The primary target is training managers or others who are responsible for choosing to hire companies to produce their training media e.g. video. This will usually be a large spend so they need to have confidence.

Industry/Entity Type

Training

Contact Information for Business Card

FRONT:

Brisk Lesson Studio
Phone: 03 5172 4039
1st Floor, 418 Kellerby Road
Mt Ferncombe
VIC 3862
Australia
www.brisklesson.com.au

Lionel Petch
Founder and Lead Consultant
mobile: +61 3 0462 735 218
email: lionel@brisklesson.com.au

BACK:
Specialising in design and production of training:

video
animation
illustration
text

for delivery via internet, intranet and/or LMS.

Number of Pages Required

4 page

Font styles to use
Sans Serif

Requirements
Must have
• The black logo uploaded with the brief.
Nice to have
• The inclusion of the shade of orange found in the orange logo also uploaded with the brief. One example would be having the back of the card in this orange and using a white font for the text. But I want the designer to work this out.
Should not have
• No colours other than black and the orange included in the uploaded orange logo.

```html
<!DOCTYPE html>
<html lang="en">
<head>
<meta charset="utf-8">
<title>Brisk Lesson Studio – Business Cards</title>
<link rel="stylesheet" href="https://fonts.googleapis.com/css2?family=Montserrat:wght@400;500;700&display=swap">
<style>
  :root {
    --stage: #2b2b2b;
    --card: #050505;
    --orange: #f15a22;
    --white: #ffffff;
    --muted: #e6e6e6;
  }
  * { box-sizing: border-box; margin: 0; padding: 0; }
  html, body {
    width: 1200px; height: 900px; overflow: hidden;
    background: var(--stage);
    font-family: "Montserrat", sans-serif;
  }
  .canvas { position: relative; width: 1200px; height: 900px; }
  .card {
    position: absolute; width: 630px; height: 360px;
    background: var(--card); border-radius: 22px; overflow: hidden;
    box-shadow: 0 18px 40px rgba(0,0,0,.55);
  }
  .card--back { left: 60px; top: 70px; }
  .card--front { left: 510px; top: 470px; }

  /* back */
  .back-brand {
    position: absolute; left: 0; right: 0; top: 90px;
    display: flex; align-items: center; justify-content: center; gap: 14px;
  }
  .brand-dot {
    width: 26px; height: 26px; border-radius: 50%;
  }
  .brand-name {
    font-weight: 700; font-size: 34px; letter-spacing: .5px;
  }
  .back-brand .brand-dot { background: var(--orange); }
  .back-brand .brand-name { color: var(--orange); }
  .services {
    position: absolute; left: 0; right: 0; top: 218px;
    text-align: center; color: var(--white); font-size: 21px; font-weight: 400;
  }
  .services .sep { color: var(--orange); padding: 0 4px; }
  .back-web {
    position: absolute; left: 0; right: 0; top: 252px;
    text-align: center; color: var(--white); font-size: 17px;
  }
  .accent { color: var(--orange); }

  /* front */
  .front-curve { position: absolute; inset: 0; }
  .front-brand {
    position: absolute; left: 400px; top: 96px; width: 220px;
    display: flex; flex-direction: column; align-items: center; gap: 10px;
  }
  .front-brand .brand-dot { background: var(--white); width: 22px; height: 22px; }
  .front-brand .brand-name { color: var(--white); font-size: 25px; text-align: center; line-height: 1.2; }
  .contact { position: absolute; left: 50px; top: 118px; color: var(--white); }
  .contact__name { color: var(--orange); font-weight: 700; font-size: 25px; }
  .contact__title { font-size: 14px; margin-top: 2px; color: var(--muted); }
  .contact__address { font-size: 14px; line-height: 1.3; margin: 8px 0 0 18px; color: var(--muted); }
  .contact__list { list-style: none; margin-top: 8px; }
  .contact__list li {
    display: flex; align-items: center; gap: 10px;
    font-size: 14px; line-height: 1.45; color: var(--muted);
  }
  .icon { width: 13px; height: 13px; flex: none; }
</style>
</head>
<body>
<main class="canvas">

  <section class="card card--back">
    <div class="back-brand">
      <span class="brand-dot"></span>
      <span class="brand-name">Brisk Lesson Studio</span>
    </div>
    <p class="services">Video<span class="sep">-</span>Animation<span class="sep">-</span>Illustration<span class="sep">-</span>Text</p>
    <p class="back-web">www.<span class="accent">brisklesson</span>.com.au</p>
  </section>

  <section class="card card--front">
    <svg class="front-curve" width="630" height="360" viewBox="0 0 630 360" aria-hidden="true">
      <path d="M150 0 C370 8 500 170 420 360" fill="none" stroke="var(--white)" stroke-width="10"/>
      <path d="M135 14 C350 24 480 180 398 360" fill="none" stroke="var(--orange)" stroke-width="9"/>
    </svg>

    <div class="front-brand">
      <span class="brand-dot"></span>
      <span class="brand-name">Brisk Lesson<br>Studio</span>
    </div>

    <div class="contact">
      <h1 class="contact__name">Lionel Petch</h1>
      <p class="contact__title">Founder and Lead Consultant</p>
      <p class="contact__address">1st Floor, 418 Kellerby Road<br>Mt Ferncombe<br>VIC 3862</p>
      <ul class="contact__list">
        <li>
          <svg class="icon" viewBox="0 0 16 16"><path d="M3 1l3 3-2 2c1 2 3 4 5 5l2-2 3 3-2 3C6 14 2 10 1 3z" fill="var(--orange)"/></svg>
          03 5172 4039
        </li>
        <li>
          <svg class="icon" viewBox="0 0 16 16"><rect x="4" y="1" width="8" height="14" rx="1.5" fill="none" stroke="var(--orange)" stroke-width="2"/></svg>
          +61 3 0462 735 218
        </li>
        <li>
          <svg class="icon" viewBox="0 0 16 16"><rect x="1" y="3" width="14" height="10" fill="none" stroke="var(--orange)" stroke-width="1.8"/><path d="M1 3l7 6 7-6" fill="none" stroke="var(--orange)" stroke-width="1.8"/></svg>
          lionel@brisklesson.com.au
        </li>
        <li>
          <svg class="icon" viewBox="0 0 16 16"><circle cx="8" cy="8" r="7" fill="none" stroke="var(--orange)" stroke-width="1.6"/><path d="M1 8h14M8 1c-3 4-3 10 0 14M8 1c3 4 3 10 0 14" fill="none" stroke="var(--orange)" stroke-width="1.3"/></svg>
          www.<span class="accent">brisklesson</span>.com.au
        </li>
      </ul>
    </div>
  </section>

</main>
</body>
</html>
```